Kettle Ledger Business Card design

We need a stand out business card design for Accounting practice based in Australia specialising in pubs, clubs and hotels. We help venues maximise margins, create time and manage cashflow. One club we have been working with for the last 6 months has increased revenue by 3% and margin by 5% in this time frame. We have a back office outsourced system that costs less than having a full time employee and also allows the venues the added benefit of:<br/>-using the office space to become a revenue generating opportunity. <br/>-a complete system to enhance governance, accountability and efficiency within their operation<br/>-52 weeks cover so no hassle to cover annual/sick .. leave<br/><br/>We would like to see designs that use the colours of our logo (green & blue).
Target Market(s)
Australian Pubs, Clubs & Hotels abookkeeping, accounting and tax services
Industry/Entity Type
Accountant
Contact Information for Business Card
Miriam Oakley CPA
Principal
Accountant Tax Agent
Miriam@KettleLedger-example.com.au
0418693142
www.kettleledger-example.com.au
Accounting / Payroll / Tax / SMSF / Technology
Colors
Designer to choose colors to be used in the design.
Look and feel
Each slider illustrates characteristics of the customer's brand and the style your logo design should communicate.

```html
<!DOCTYPE html>
<html lang="en">
<head>
<meta charset="UTF-8">
<title>Kettle Ledger Business Card</title>
<link rel="stylesheet" href="https://fonts.googleapis.com/css2?family=Montserrat:wght@500;700;800&family=Roboto:wght@400&display=swap">
<style>
  :root {
    --green: #1e7d45;
    --green-deep: #17703c;
    --blue: #24398f;
    --white: #ffffff;
    --grey-text: #6b6b6b;
    --backdrop: #e4e4e4;
  }
  * { margin: 0; padding: 0; box-sizing: border-box; }
  html, body { width: 1200px; height: 930px; overflow: hidden; }
  body {
    background: var(--backdrop);
    font-family: "Montserrat", Arial, sans-serif;
    position: relative;
  }
  .card {
    position: absolute;
    width: 520px;
    height: 300px;
    border-radius: 22px;
    overflow: hidden;
    box-shadow: 0 6px 18px rgba(0,0,0,0.18);
  }
  /* Front */
  .card-front {
    left: 80px; top: 110px;
    background: var(--green);
    color: var(--white);
  }
  .front-brand {
    position: absolute;
    left: 0; right: 0; top: 92px;
    display: flex; align-items: center; justify-content: center; gap: 18px;
  }
  .brand-dot {
    width: 58px; height: 58px; border-radius: 50%;
    border: 4px solid var(--white);
  }
  .front-name {
    font-weight: 800; font-size: 44px; letter-spacing: -0.5px; line-height: 1;
    color: var(--white);
  }
  .services {
    position: absolute; left: 34px; bottom: 30px;
    font-weight: 700; font-size: 17px; letter-spacing: 0.3px;
  }
  /* Back */
  .card-back {
    left: 600px; top: 500px;
    background: var(--white);
  }
  .back-name {
    position: absolute; left: 34px; top: 38px;
    font-weight: 800; font-size: 34px; letter-spacing: -0.5px; line-height: 1;
    color: var(--blue);
  }
  .back-mark {
    position: absolute; left: 370px; top: 30px;
    width: 110px; height: 110px; border-radius: 50%;
    border: 5px solid var(--green);
  }
  .guide-line { position: absolute; left: 0; top: 0; }
  .holder {
    position: absolute; left: 50px; top: 148px;
  }
  .holder-name {
    font-weight: 800; font-size: 20px; line-height: 24px; letter-spacing: 1px; color: var(--green);
  }
  .holder-name .credential { color: var(--blue); }
  .holder-role {
    font-family: "Roboto", Arial, sans-serif; font-size: 15px; line-height: 20px; color: var(--grey-text); margin-top: 2px;
  }
  .contact-list {
    list-style: none; margin-top: 12px;
    font-family: "Roboto", Arial, sans-serif; font-size: 14.5px; color: var(--grey-text);
  }
  .contact-list li { display: flex; align-items: center; gap: 9px; margin-bottom: 3px; }
  .contact-list svg { width: 13px; height: 13px; flex: none; }
  .base-band { position: absolute; left: 0; bottom: 0; }
</style>
</head>
<body>

<section class="card card-front" aria-label="Card front">
  <div class="front-brand">
    <span class="brand-dot"></span>
    <span class="front-name">Kettle Ledger</span>
  </div>
  <p class="services">Accounting | Payroll | Tax | SMSF | Technology</p>
</section>

<section class="card card-back" aria-label="Card back">
  <p class="back-name">Kettle Ledger</p>
  <span class="back-mark"></span>
  <svg class="guide-line" width="520" height="300" viewBox="0 0 520 300">
    <polyline points="124,185 305,185 386,124" fill="none" stroke="var(--green)" stroke-width="1.2"/>
  </svg>
  <div class="holder">
    <p class="holder-name">MIRIAM OAKLEY <span class="credential">CPA</span></p>
    <p class="holder-role">Principal</p>
    <ul class="contact-list">
      <li><svg viewBox="0 0 24 24"><path d="M6 2l4 4-2 3c1 3 4 6 7 7l3-2 4 4-3 4C10 22 2 14 2 5z" fill="var(--green)"/></svg>0418693142</li>
      <li><svg viewBox="0 0 24 24"><rect x="2" y="5" width="20" height="14" fill="none" stroke="var(--green)" stroke-width="2.4"/><path d="M2 6l10 7 10-7" fill="none" stroke="var(--green)" stroke-width="2.4"/></svg>Miriam@KettleLedger-example.com.au</li>
      <li><svg viewBox="0 0 24 24"><circle cx="12" cy="12" r="10" fill="var(--green)"/><path d="M2 12h20M12 2c-4 5-4 15 0 20M12 2c4 5 4 15 0 20" fill="none" stroke="var(--white)" stroke-width="1.4"/></svg>www.kettleledger-example.com.au</li>
    </ul>
  </div>
  <svg class="base-band" width="520" height="14" viewBox="0 0 520 14">
    <polygon points="0,0 330,0 326,14 0,14" fill="var(--green)"/>
    <polygon points="334,0 520,0 520,14 330,14" fill="var(--blue)"/>
  </svg>
</section>

</body>
</html>
```